Business Card Design

We need a business card design for a Non-Profit Christian Based Organization located in Milford, Pa.
Alder Ridge Helping Harbor
Is a Christ-centered organization dedicated to providing compassion and hope to homeless or near homeless, families and individuals, by meeting their basic and urgent need of food, clothing and shelter.
Updates
the logo is black and white
and must add the color green some where 00400
Industry/Entity Type
Clothing
Contact Information for Business Card
Alder Ridge Helping Harbor
P.O. Box 287
Milord, Pa 18337
Phone: (570) 413-CARE(2273)
Toll Free: (855) 413-CARE
email:Info@alderridgehh.org
email:Careline@alderridgehh.org
Our organization already has a logo.
Front of card:
Is a Christ-centered organization dedicated to providing compassion and hope to homeless or near homes, families and individual by meeting their basic and urgent need of food, clothing and shelter.(this is our Mission Statement)
On back of card:
'I was hungry and you gave me something to eat;
"I was thirsty and you gave me something to drink;
"I was a stranger and you invited me in."
Matthew 25:35
Color: Logo is black and white
Background color I would like a bright light green 00ff00(close to that)
I attached a sample of what I created on Quill Press but, I don't like the color green, nor the design (but I just wanted to give you and Idea of the Logo and Alder Ridge (one line) Helping Harbor (second line) in a different font thank you
Delia Rostova
Pr/Board of Directors

```html
<!DOCTYPE html>
<html lang="en">
<head>
<meta charset="utf-8">
<title>Alder Ridge Helping Harbor – Business Card</title>
<link rel="stylesheet" href="https://fonts.googleapis.com/css2?family=Sniglet&family=Source+Sans+3:wght@700&display=swap">
<style>
  :root {
    --paper: #ffffff;
    --ink: #111111;
    --lime: #a8ff00;
    --page: #ffffff;
  }
  html, body {
    margin: 0;
    padding: 0;
    width: 1200px;
    height: 702px;
    overflow: hidden;
    background: var(--page);
  }
  .card {
    position: relative;
    width: 1200px;
    height: 702px;
    display: flex;
    color: var(--ink);
  }
  .card__info {
    width: 586px;
    height: 100%;
    background: var(--paper);
    position: relative;
  }
  .mission {
    position: absolute;
    top: 70px;
    left: 20px;
    width: 560px;
    margin: 0;
    text-align: center;
    font-family: "Sniglet", "Comic Sans MS", cursive;
    font-size: 33px;
    line-height: 45px;
  }
  .contacts {
    position: absolute;
    left: 0;
    width: 586px;
    margin: 0;
    padding: 0;
    list-style: none;
    text-align: center;
    font-family: "Source Sans 3", "Myriad Pro", sans-serif;
    font-weight: 700;
    font-size: 25px;
    line-height: 36px;
  }
  .contacts--phone { top: 470px; }
  .contacts--email { top: 566px; }
  .contacts li::before { content: "\2022"; }

  .card__brand {
    flex: 1;
    height: 100%;
    background: var(--lime);
    position: relative;
  }
  .brand__square {
    position: absolute;
    left: 157px;
    top: 64px;
    width: 317px;
    height: 414px;
    background: var(--paper);
  }
  .brand__name {
    position: absolute;
    left: 0;
    width: 614px;
    top: 502px;
    margin: 0;
    text-align: center;
    font-family: "Source Sans 3", "Myriad Pro", sans-serif;
    font-weight: 700;
    color: var(--ink);
    text-transform: uppercase;
    font-size: 58px;
    line-height: 72px;
  }
  .brand__name span { display: block; }
</style>
</head>
<body>
  <main class="card">
    <section class="card__info">
      <p class="mission">a Christ-centered organization dedicated to providing compassion and hope to homeless or near homes, families and individual by meeting their basic and urgent need of food, clothing and shelter</p>
      <ul class="contacts contacts--phone">
        <li>Phone: (570) 413-CARE (2273)</li>
        <li>Toll Free: (855) 413-CARE</li>
      </ul>
      <ul class="contacts contacts--email">
        <li>Email:Info@alderridgehh.org</li>
        <li>Email:Careline@alderridgehh.org</li>
      </ul>
    </section>
    <section class="card__brand">
      <div class="brand__square" aria-hidden="true"></div>
      <h1 class="brand__name"><span>Alder Ridge</span><span>Helping Harbor</span></h1>
    </section>
  </main>
</body>
</html>
```